Point of Sale Systems Web Design Project

I need a complete redesign of my existing website. I sell point of sale systems and need to seamlessly combine the features, products and services of several companies I represent. The current site is at www.tillgroveplaza.com. The new site will be rebranded as www.TradeZoral.com. I will be adding products from www.quaylinkpro.com, www.pinrowly.com, www.dakswivo.com as well as other similar products and services such as http://kelbafund.com/homepage_USA.html

The new tag line will be:
Electronic Payment Systems Made ZORAL!
Updates

I have made a change to the website name. The new name will be TradeZoral.com. I look forward to seeing the designs. Please see http://www.zoral.com.au/index.html for the inspiration behind the new name. I am also going to increase the budget for this project. Thank you

Target Market(s)

These are products and services for business owners. We provide Credit Card Processing Equipment and Processing Services to Retail, Restaurant, Home-based, and Internet businesses.

Industry/Entity Type

Electronic

Requirements
Must have
• Visitors need to be able to view video demos and download PDF documents. Site should be easy to update with new products or services.
Nice to have
• Designs I like: http://www.thebrivelworks.com, http://www.plantyourbalconies.com, http://www.qortalvistagroup.com/

```html
<!DOCTYPE html>
<html lang="en">
<head>
<meta charset="utf-8">
<title>TradeZoral.com – Electronic Payment Solutions</title>
<link rel="stylesheet" href="https://fonts.googleapis.com/css2?family=Questrial&display=swap">
<style>
:root{
  --blue:#0aa9ee;
  --blue-dark:#0b86c4;
  --ink:#222;
  --text:#333;
  --white:#fff;
  --card:#606060;
  --panel:#dddddd;
  --hero:#cfcfcf;
  --red:#b8322a;
  --line:#d6d6d6;
}
*{box-sizing:border-box;margin:0;padding:0}
html,body{width:1069px;height:1200px;overflow:hidden;background:var(--white)}
body{font-family:"Questrial",Arial,sans-serif;color:var(--text);position:relative}
.page{position:relative;width:1069px;height:1200px}
.abs{position:absolute}

/* header */
.site-header{left:22px;top:0;width:1025px;height:100px;background:var(--blue);border-radius:0 0 4px 4px}
.brand{left:20px;top:22px;display:flex;align-items:center;gap:8px;font-size:38px;color:var(--ink);letter-spacing:1px}
.brand-mark{width:30px;height:30px;background:var(--ink)}
.phone{left:675px;top:24px;font-size:25px;color:var(--white)}
.social{left:873px;top:26px;display:flex;gap:7px}
.social span{width:21px;height:21px;background:var(--white);opacity:.85;border-radius:3px}
.social svg{display:block}
.main-nav{right:20px;top:68px;display:flex;font-size:21px;color:var(--white)}
.main-nav a{color:inherit;text-decoration:none;padding:0 11px;border-left:1px solid rgba(255,255,255,.8);line-height:22px}
.main-nav a:first-child{border-left:none}
.rule{height:3px;background:linear-gradient(90deg,transparent,#c8c8c8 20%,#c8c8c8 80%,transparent)}

/* hero */
.hero{left:22px;top:135px;width:1023px;height:345px;background:linear-gradient(180deg,#dcdcdc,#bdbdbd);border-radius:6px;overflow:hidden}
.hero-photo{left:0;top:0;width:700px;height:345px;background:linear-gradient(100deg,#8d7b6d 0%,#b9aca2 35%,#d9d9d9 70%,#cfcfcf 100%)}
.hero-title{left:0;top:10px;width:100%;text-align:center;font-size:42px;color:var(--ink);font-weight:400}
.hero-panel{left:410px;top:70px;width:613px;height:275px;background:var(--white);border-radius:6px 0 0 0;padding:22px 26px}
.hero-panel h2{font-size:32px;font-weight:400;color:var(--blue);margin-bottom:16px}
.hero-panel p{font-size:13.3px;line-height:16.5px;color:var(--ink)}
.btn{display:flex;align-items:center;height:36px;border-radius:4px;background:linear-gradient(#fafafa,#dedede);box-shadow:0 2px 3px rgba(0,0,0,.35);color:var(--ink)}
.btn-terminal{left:26px;top:224px;width:145px;padding-left:10px;font-size:16px}
.btn-process{left:180px;top:224px;width:142px;padding-left:8px;font-size:12px;gap:12px}
.pdf{right:26px;top:208px;text-align:center;font-size:11px;color:var(--ink)}
.pdf span{display:block;width:30px;height:32px;margin:0 auto 4px;background:#f2f2f2;border:1px solid #bbb;border-top:6px solid #c22}

/* feature cards */
.card{top:514px;width:316px;height:292px;background:var(--card);border-radius:5px;color:var(--white);padding:14px 20px}
.card h3{font-size:18.5px;font-weight:400;line-height:24px;margin-bottom:4px}
.card p{font-size:13.3px;line-height:17px}
.card .notch{right:-14px;top:128px}
.card-img{background:linear-gradient(135deg,#f4f4f4,#9aa3ab)}
.video-btn{left:20px;bottom:12px;width:88px;height:23px;background:linear-gradient(#fff,#ddd);border-radius:3px;color:#444;font-size:11px;display:flex;align-items:center;padding-left:6px;gap:6px}
.card-logo{left:16px;top:125px;font-size:22px;color:#9a9a9a;letter-spacing:1px}

/* quote form */
.quote{left:19px;top:841px;width:388px;height:290px;border:1px solid var(--line);background:var(--white)}
.quote h4{left:0;width:100%;text-align:right;padding-right:68px;font-weight:400;font-size:21px;color:var(--red)}
.quote label{left:10px;font-size:13px;color:var(--ink)}
.field{left:152px;width:223px;height:24px;border:1px solid #ddd;background:#fff}
.select{font-size:11px;padding:4px 8px;color:#333;background:#f7f7f7}
.select i{position:absolute;right:0;top:0;width:20px;height:22px;background:#d4d4d4}

/* news */
.news{left:432px;top:841px;width:613px;height:292px;background:var(--panel);border-radius:6px}
.news h3{left:26px;font-size:21px;font-weight:400;color:var(--blue)}
.news .thumb{left:28px;width:94px;height:76px;border:1px solid #999}
.news .item{left:142px;width:450px;font-size:13.3px;line-height:16.3px;color:var(--ink)}
.news .more{right:20px;font-size:13px;color:var(--red)}

/* footer */
.site-footer{left:0;top:1146px;width:1069px;height:54px;background:var(--blue)}
.footer-brand{left:18px;top:12px;font-size:26px;color:#3a3a3a}
.footer-note{left:200px;top:19px;font-size:12.3px;color:var(--white);display:flex;align-items:center;gap:10px}
.copy{width:15px;height:15px;border:1.5px solid var(--white);border-radius:50%;font-size:9px;display:flex;align-items:center;justify-content:center}
</style>
</head>
<body>
<div class="page">

  <header class="site-header abs">
    <div class="brand abs"><span class="brand-mark"></span>TradeZoral.com</div>
    <div class="phone abs">888-555-0142</div>
    <div class="social abs">
      <span></span><span></span><span></span><span></span>
      <svg width="24" height="21" viewBox="0 0 24 21"><rect x="1" y="3" width="22" height="15" fill="#fff" stroke="#9ab" /><path d="M1 3l11 8 11-8" fill="none" stroke="#9ab"/></svg>
    </div>
    <nav class="main-nav abs">
      <a href="#">Home</a><a href="#">About</a><a href="#">Solutions</a><a href="#">Services</a><a href="#">Equipment</a><a href="#">Contact</a>
    </nav>
  </header>
  <div class="rule abs" style="left:160px;top:110px;width:750px"></div>

  <section class="hero abs">
    <div class="hero-photo abs" role="img" aria-label="Hands typing a card payment on a laptop keyboard"></div>
    <h1 class="hero-title abs">Electronic Payment Solutions Made ZORAL!</h1>
    <div class="hero-panel abs">
      <h2>POS Technology, Systems And Solutions</h2>
      <p>No storefront. No problem. Do you have a PC or Laptop connected to the internet?<br>
      Start processing credit card transactions from any computer with an internet connection.
      Manually process mail and telephone credit&nbsp; card transactions or swipe card via a USB card swiper. Just like a traditional terminal, but with the added flexubility of giving you access from any interne connection in the world.<br>
      There's no hardware to purchase&nbsp; or soft to download. It's flexible, low-cost and trouble free.</p>
      <a class="btn btn-terminal abs">Virtual Treminal</a>
      <a class="btn btn-process abs">Process Payments
        <svg width="20" height="20" viewBox="0 0 20 20"><circle cx="10" cy="10" r="9" fill="#1d76b8"/><path d="M8 5l5 5-5 5z" fill="#fff"/></svg>
      </a>
      <div class="pdf abs"><span></span>PDF&nbsp; Details</div>
    </div>
  </section>
  <div class="rule abs" style="left:160px;top:500px;width:750px"></div>

  <article class="card abs" style="left:21px">
    <h3>Pinrowly Salon</h3>
    <p>software does everything you've come to expect rom a salon software POS system - and so much more.<br>The simple touch screen and finger-friendly salon software design will have you moving at salon speed in no time.</p>
    <div class="card-img abs" role="img" aria-label="Salon touchscreen POS terminal with printer" style="left:78px;top:162px;width:152px;height:84px"></div>
    <svg class="notch abs" width="18" height="44" viewBox="0 0 18 44"><path d="M0 0q18 22 0 44z" fill="#606060"/></svg>
    <a class="video-btn abs">View video <svg width="16" height="10" viewBox="0 0 16 10"><path d="M0 0l7 5-7 5zM8 0l7 5-7 5z" fill="#1d76b8"/></svg></a>
  </article>

  <article class="card abs" style="left:365px">
    <h3>Complet and Affordable POS Solutions for Retai and Hospitality Merchants!</h3>
    <p style="margin-top:10px">Choose from a variety of accessories that are designed specifically with the retail and restaurante environment!</p>
    <div class="card-img abs" role="img" aria-label="Retail POS monitor, card terminal and receipt printer" style="left:82px;top:168px;width:176px;height:100px;background:linear-gradient(135deg,#2a6fc4,#0b2f66)"></div>
    <svg class="notch abs" width="18" height="44" viewBox="0 0 18 44"><path d="M0 0q18 22 0 44z" fill="#606060"/></svg>
    <a class="video-btn abs">View video <svg width="16" height="10" viewBox="0 0 16 10"><path d="M0 0l7 5-7 5zM8 0l7 5-7 5z" fill="#1d76b8"/></svg></a>
  </article>

  <article class="card abs" style="left:710px">
    <h3>Accepting Credit Cards Has Never Been Easier.</h3>
    <p style="margin-top:4px">Dak Swivo is a free app and free credit card reader that transforms your smartphone into a mobile point-of-sale terminal.</p>
    <div class="card-logo abs">dakswivo</div>
    <div class="card-img abs" role="img" aria-label="Smartphones fitted with a card reader" style="left:74px;top:165px;width:182px;height:90px"></div>
    <svg class="notch abs" width="18" height="44" viewBox="0 0 18 44"><path d="M0 0q18 22 0 44z" fill="#606060"/></svg>
    <a class="video-btn abs">View video <svg width="16" height="10" viewBox="0 0 16 10"><path d="M0 0l7 5-7 5zM8 0l7 5-7 5z" fill="#1d76b8"/></svg></a>
  </article>
  <div class="rule abs" style="left:160px;top:818px;width:750px"></div>

  <form class="quote abs">
    <svg class="abs" style="left:64px;top:-10px" width="112" height="48" viewBox="0 0 112 48"><defs><linearGradient id="arrowFill" x1="0" y1="0" x2="0" y2="1"><stop offset="0" stop-color="#3cc3f7"/><stop offset="1" stop-color="#0b86c4"/></linearGradient></defs><path d="M8 0h96v12l-48 36L0 12z" fill="url(#arrowFill)"/></svg>
    <h4 class="abs" style="top:46px">Get a FREE quote!</h4>
    <label class="abs" style="top:96px">Full name:</label>
    <div class="field abs" style="top:80px"></div>
    <label class="abs" style="top:122px">Email:</label>
    <div class="field abs" style="top:106px"></div>
    <label class="abs" style="top:148px">Phone:</label>
    <div class="field abs" style="top:132px"></div>
    <label class="abs" style="top:172px">Type of inquires:</label>
    <div class="field select abs" style="top:158px">Select<i></i></div>
    <label class="abs" style="top:242px">Additional information:</label>
    <div class="field abs" style="top:190px;height:60px"></div>
    <h4 class="abs" style="top:261px;padding-right:80px">Get Quote Now!</h4>
  </form>

  <section class="news abs">
    <h3 class="abs" style="top:30px">Gift Cards</h3>
    <div class="thumb abs" role="img" aria-label="Stack of gift cards" style="top:62px;background:linear-gradient(135deg,#e9eef6,#3b66b3)"></div>
    <p class="item abs" style="top:64px">1.06.2011<br>Quisque vitae pede.<br>Nam et augue. Sed a elit.Ut vel massa. Suspendisse nibh pede, ultrices vitae, ltrices nec... Nam et augue. Sed a elit.Ut vel massa. Suspendisse nibh pede, ultrices vitae, ltrices nec..</p>
    <a class="more abs" style="top:138px">Learn more...</a>
    <h3 class="abs" style="top:162px">Merchant Cash Advance</h3>
    <div class="thumb abs" role="img" aria-label="Hand paying with a card at a terminal" style="top:193px;background:linear-gradient(135deg,#c9b8a6,#6c5b4e)"></div>
    <p class="item abs" style="top:196px">3.06.2011<br>Quisque vitae pede.<br>Nam et augue. Sed a elit.Ut vel massa. Suspendisse nibh pede, ultrices vitae, ltrices nec... Nam et augue. Sed a elit.Ut vel massa. Suspendisse nibh pede, ultrices vitae, ltrices nec..</p>
    <a class="more abs" style="top:268px">Learn more...</a>
  </section>

  <footer class="site-footer abs">
    <div class="footer-brand abs">billvanta</div>
    <div class="footer-note abs"><span class="copy">c</span>Corvane Acceptance Systems Registered Sales Agent for Tallowmere Payments Inc. Member Bank: Brightwater Bank N.A., Elmsford Creek, CA - Member.FDIC</div>
  </footer>

</div>
</body>
</html>
```